Business Card Design - Construction Company

Tarrowin Construction is in need of a sharp, modern business card design that has an architectural/high fashion feel.

We are looking for a two sided card.

One side simple dark grey/black with some texture in the background. e.g. (a mosaic of simple interconnecting shapes or a shadow of the logo.) Something to draw attention and create interest.It will need to feature a large Tarrowin construction logo (files attached) in metallic gradient or plain white.

The other side should contain all of our information:

(in largest text)
Name of person
Tarrowin Construction Pty. Ltd.

Licensed builders specialising in:
- Bathrooms
- Kitchens
- Commercial interiors

(mid sized text)
Phone number
Fax number
person@tarrowinconstruction.example.au
www. tarrowinconstruction.example.au

(smaller text)
ABN: 62407938215
BSA license: xxx-xxxx
PO Box 8641 Kellsmoor QLD 4019 (address)

Target Market(s)

professional home and business owners

Industry/Entity Type

Construction

Requirements
Must have
• Must be bold, professional looking and modern.
Nice to have
• We are undecided as to what kind of printing we will go with.
Definitely square edged.
Probably high quality satin card.
We are also interested in designs that would work well on transparent or translucent plastic.
Ideally we would print two versions.
Should not have
• Nothing with an antique feel.
No wild colours. Small amounts of colour can be good in the right place.

```html
<!DOCTYPE html>
<html lang="en">
<head>
<meta charset="utf-8">
<title>Tarrowin Construction – Business Card</title>
<link rel="stylesheet" href="https://fonts.googleapis.com/css2?family=Open+Sans:ital,wght@0,400;0,600;0,700;1,400;1,600;1,700&display=swap">
<style>
  :root {
    --page: #ffffff;
    --card: #ffffff;
    --card-dark: #1f1f21;
    --card-dark-2: #2e2e31;
    --texture: rgba(255, 255, 255, 0.045);
    --ink: #2b2b2b;
    --ink-soft: #444444;
    --ink-fine: #555555;
    --mark-grey: #6d6d6d;
    --mark-light: #f2f2f2;
    --panel-dark: #6f6f73;
    --panel-light: #e4e4e6;
    --shadow: rgba(0, 0, 0, 0.35);
  }
  * { box-sizing: border-box; margin: 0; padding: 0; }
  html, body {
    width: 893px;
    height: 1200px;
    overflow: hidden;
    background: var(--page);
    font-family: "Open Sans", Arial, sans-serif;
    color: var(--ink);
  }
  .canvas { position: relative; width: 893px; height: 1200px; }

  .card {
    position: absolute;
    width: 488px;
    height: 265px;
    background: var(--card);
    box-shadow: 2px 3px 8px var(--shadow);
    overflow: hidden;
  }
  .card--front {
    left: 69px; top: 58px;
    background:
      repeating-linear-gradient(60deg, var(--texture) 0 1px, transparent 1px 22px),
      repeating-linear-gradient(-60deg, var(--texture) 0 1px, transparent 1px 22px),
      repeating-linear-gradient(0deg, var(--texture) 0 1px, transparent 1px 19px),
      radial-gradient(ellipse at 50% 35%, var(--card-dark-2) 0%, var(--card-dark) 75%);
  }
  .card--back { left: 346px; top: 368px; }

  .card__band { position: absolute; left: 0; bottom: 0; width: 100%; height: 60px; }

  .card__panel {
    position: absolute;
    border-radius: 6px;
    background: linear-gradient(180deg, var(--panel-light) 0%, var(--panel-dark) 50%, var(--panel-light) 100%);
    box-shadow: 0 2px 4px rgba(0,0,0,0.3);
  }
  .card--front .card__panel { left: 198px; top: 124px; width: 92px; height: 112px; }
  .card--back .card__panel { left: 204px; top: 121px; width: 86px; height: 138px; }

  .brand { position: absolute; left: 0; width: 100%; text-align: center; color: var(--mark-grey); }
  .brand__dot { display: block; margin: 0 auto; border-radius: 50%; background: var(--mark-grey); }

  .card--front .brand { top: 22px; color: var(--mark-light); }
  .card--front .brand__dot { width: 54px; height: 54px; background: var(--mark-light); }
  .card--front .brand__name { display: block; margin-top: 10px; font-size: 20px; font-weight: 700; letter-spacing: 1.5px; line-height: 1; }

  .card--back .brand { top: 12px; }
  .card--back .brand__dot { width: 66px; height: 66px; }
  .card--back .brand__name { display: block; margin-top: 10px; font-size: 20px; font-weight: 700; letter-spacing: 0.5px; line-height: 1; }
  .card--back .brand__sub { display: block; margin-top: 1px; font-size: 7.5px; font-weight: 700; letter-spacing: 2px; line-height: 1.3; }

  .services {
    position: absolute;
    right: 292px;
    top: 167px;
    list-style: none;
    text-align: right;
    font-size: 10px;
    line-height: 13px;
    color: var(--ink);
  }
  .services li::after {
    content: "";
    display: inline-block;
    width: 4px; height: 4px;
    margin-left: 5px;
    vertical-align: middle;
    background: var(--ink);
  }

  .contact { position: absolute; left: 300px; top: 128px; color: var(--ink); }
  .contact__name { font-size: 12.5px; font-weight: 700; font-style: italic; line-height: 15px; }
  .contact__company { font-size: 10px; font-style: italic; color: var(--ink-soft); line-height: 13px; }
  .contact__phones { margin-top: 9px; font-size: 10px; line-height: 13px; }
  .contact__phones b { font-weight: 700; }
  .contact__phones .gap { display: inline-block; width: 8px; }
  .contact__line { font-size: 9px; line-height: 11px; }
  .contact__fine { margin-top: 3px; font-size: 7px; line-height: 8.5px; color: var(--ink-fine); }
</style>
</head>
<body>
<div class="canvas">

  <section class="card card--front" aria-label="Card front">
    <div class="brand">
      <span class="brand__dot"></span>
      <span class="brand__name">TARROWIN</span>
    </div>
    <svg class="card__band" viewBox="0 0 488 60" preserveAspectRatio="none" aria-hidden="true">
      <defs>
        <linearGradient id="bandFront" x1="0" x2="1" y1="0" y2="0">
          <stop offset="0" stop-color="#0c0c0c"/>
          <stop offset="0.5" stop-color="#2a2a2a"/>
          <stop offset="0.85" stop-color="#5e5e5e"/>
          <stop offset="1" stop-color="#8c8c8c"/>
        </linearGradient>
      </defs>
      <path d="M0 60 L0 52 Q244 6 488 52 L488 60 Z" fill="url(#bandFront)"/>
    </svg>
    <div class="card__panel" role="img" aria-label="Ornate metallic mosaic panel"></div>
  </section>

  <section class="card card--back" aria-label="Card back">
    <div class="brand">
      <span class="brand__dot"></span>
      <span class="brand__name">TARROWIN</span>
      <span class="brand__sub">CONSTRUCTION</span>
    </div>
    <svg class="card__band" viewBox="0 0 488 60" preserveAspectRatio="none" aria-hidden="true">
      <defs>
        <linearGradient id="bandBack" x1="0" x2="1" y1="0" y2="0">
          <stop offset="0" stop-color="#1e1e1e"/>
          <stop offset="0.45" stop-color="#3a3a3a"/>
          <stop offset="0.8" stop-color="#8a8a8a"/>
          <stop offset="1" stop-color="#d9d9d9"/>
        </linearGradient>
      </defs>
      <path d="M0 60 L0 52 Q244 6 488 52 L488 60 Z" fill="url(#bandBack)"/>
    </svg>
    <div class="card__panel" role="img" aria-label="Ornate metallic mosaic panel"></div>

    <ul class="services">
      <li>Bathrooms</li>
      <li>Kitchens</li>
      <li>Commercial interiors</li>
    </ul>

    <div class="contact">
      <p class="contact__name">Name Name</p>
      <p class="contact__company">Tarrowin Construction Pty. Ltd.</p>
      <p class="contact__phones"><b>T:</b> 00 0000000<span class="gap"></span><b>F:</b> 00 00000000</p>
      <p class="contact__line">person@tarrowinconstruction.example.au</p>
      <p class="contact__line">www. tarrowinconstruction.example.au</p>
      <div class="contact__fine">
        <p>ABN: 62407938215 &nbsp; BSA license: xxx-xxxx</p>
        <p>PO Box 8641 Kellsmoor QLD 4019</p>
      </div>
    </div>
  </section>

</div>
</body>
</html>
```